Clean professional design needed for landscape property business

We need a logo for a new lawncare, landscaping , property maintenance business called Fernway Grove.
Our services include lawn mowing, garden maintenance, clean ups and some property maintenance.
We want a double sided business card that is clean and very professional using the colour scheme from our logo which is provided.
the business card should have impact as we will use these to drop into people's letterboxes as a marketing drop.
Initially we want to see what you come up with so there is a very wide scope here to work with.

Project Deadline Extended
Reason: we feel our original deadline was too short. we have extended to give more time for quality submissions.

Target Market(s)

High end property owners who don't wish to do there own gardneing or property maintenance

Industry/Entity Type

Business

Contact Information for Business Card

Name
Postion/ Title
Phone number
mobile
web address
physical address

services offered

Font styles to use
Sans Serif

Requirements
Must have
• curved edges preferrred
Nice to have
• We like the idea of the logo being embossed or etched into the card so it looks like it is below the surface of the card
Should not have
• No stock images or characters.

```html
<!DOCTYPE html>
<html lang="en">
<head>
<meta charset="utf-8">
<title>Fernway Grove – Business Card</title>
<link rel="stylesheet" href="https://fonts.googleapis.com/css2?family=Open+Sans:wght@400;600;700&display=swap">
<style>
  :root {
    --bg: #ecebe8;
    --card-dark: #5f6062;
    --card-dark-mark: #4b4c4e;
    --card-light: #ffffff;
    --green: #7cc242;
    --ink: #4a4a4c;
    --ink-soft: #555658;
    --white: #ffffff;
  }
  * { margin: 0; padding: 0; box-sizing: border-box; }
  html, body { width: 1200px; height: 1000px; overflow: hidden; }
  body {
    background: var(--bg);
    font-family: "Open Sans", Arial, sans-serif;
    position: relative;
  }
  .card {
    position: absolute;
    left: 266px;
    width: 666px;
    height: 398px;
    box-shadow: 0 6px 14px rgba(0,0,0,0.18);
  }
  .card--back {
    top: 74px;
    background: var(--card-dark);
    border-radius: 6px 72px 6px 72px;
  }
  .card--front {
    top: 533px;
    background: var(--card-light);
    border-radius: 72px 6px 72px 6px;
  }
  .wordmark {
    position: absolute;
    display: flex;
    align-items: center;
    gap: 18px;
    font-weight: 600;
    letter-spacing: -2px;
    white-space: nowrap;
  }
  .wordmark__square { display: block; }
  .card--back .wordmark {
    left: 108px; top: 178px;
    font-size: 54px;
    color: var(--card-dark-mark);
  }
  .card--back .wordmark__square { width: 24px; height: 24px; background: var(--card-dark-mark); }
  .card--front .wordmark {
    left: 290px; top: 86px;
    font-size: 46px;
    color: var(--ink-soft);
  }
  .card--front .wordmark__square { width: 18px; height: 18px; background: var(--ink-soft); }

  .definition {
    position: absolute;
    left: 114px; top: 322px;
    display: flex; gap: 10px;
    color: var(--white);
    font-size: 16px;
    line-height: 22px;
  }
  .definition__dot {
    width: 12px; height: 12px; margin-top: 6px;
    border-radius: 50%; background: var(--white); flex: none;
  }
  .definition p { text-align: center; }

  .person { position: absolute; left: 33px; top: 172px; color: var(--ink); }
  .person__name { color: var(--green); font-weight: 700; font-size: 20px; letter-spacing: 0.3px; line-height: 26px; }
  .person__title { font-size: 16px; line-height: 22px; }
  .address { position: absolute; left: 33px; top: 229px; font-size: 16px; line-height: 21px; color: var(--ink); font-style: normal; }
  .contacts { position: absolute; left: 33px; top: 280px; list-style: none; font-size: 16px; color: var(--ink); }
  .contacts li { display: flex; align-items: center; gap: 8px; height: 22.3px; }
  .contacts svg { width: 14px; height: 14px; flex: none; }

  .services {
    position: absolute; right: 32px; top: 196px;
    display: flex; gap: 14px; list-style: none;
    font-size: 17px; color: var(--ink);
  }
  .services li { display: flex; align-items: center; gap: 5px; }
  .services li::before {
    content: ""; width: 9px; height: 9px; border-radius: 50%; background: var(--green);
  }
</style>
</head>
<body>

<section class="card card--back" aria-label="Card back">
  <div class="wordmark">
    <span>fernwaygrove</span>
    <span class="wordmark__square"></span>
  </div>
  <div class="definition">
    <span class="definition__dot"></span>
    <p>Fernway Grove (noun) - the attractiveness of a property<br>and its surroundings when viewed from the street</p>
  </div>
</section>

<section class="card card--front" aria-label="Card front">
  <div class="wordmark">
    <span>fernwaygrove</span>
    <span class="wordmark__square"></span>
  </div>

  <div class="person">
    <h1 class="person__name">DANIEL HARTLEY</h1>
    <p class="person__title">Managing Director</p>
  </div>

  <address class="address">Level 12, 8 Harbour Point<br>Sydney, 20, New South Wales</address>

  <ul class="contacts">
    <li>
      <svg viewBox="0 0 14 14"><rect x="3" y="0.5" width="8" height="13" rx="1.5" fill="none" stroke="var(--green)" stroke-width="1.4"/><rect x="4.6" y="2.3" width="4.8" height="6" fill="var(--green)"/></svg>
      + 000 000 0000
    </li>
    <li>
      <svg viewBox="0 0 14 14"><path d="M1 5c0-2 2.5-3 6-3s6 1 6 3v1h-3V4.5H4V6H1z" fill="var(--green)"/><rect x="2.5" y="7" width="9" height="5.5" rx="1" fill="var(--green)"/></svg>
      + 000 000 0000
    </li>
    <li>
      <svg viewBox="0 0 14 14"><rect x="0.5" y="3" width="13" height="9" fill="var(--green)"/><path d="M0.5 3l6.5 5 6.5-5" fill="none" stroke="#fff" stroke-width="1.2"/></svg>
      info@fernwaygrove.com.au
    </li>
    <li>
      <svg viewBox="0 0 14 14"><circle cx="7" cy="7" r="6" fill="none" stroke="var(--green)" stroke-width="1.6"/><path d="M1 7h12M7 1c-3 3.5-3 8.5 0 12M7 1c3 3.5 3 8.5 0 12" fill="none" stroke="var(--green)" stroke-width="1.1"/></svg>
      www.fernwaygrove.com.au
    </li>
  </ul>

  <ul class="services">
    <li>Lawn</li>
    <li>Gardens</li>
  </ul>
</section>

</body>
</html>
```